Clinical Research Consulting Company needs a web design

My consulting company provides service on clinical trial design and clincal research, product safety and claim development strategy, and lecture service.

Need template and graphic design for the website of my consulting company. Website will have many different tabs (e.g., Home, About Us, Service, and Contact Us).

Like to have modern look and easy on eyes (not too many colors).

We don't perform laboratory work so please do not use pictures with people working in the laboratory. Also, the logo is added. Thanks.

Target Market(s)

Pharmaceutical and Biotech companies, dietary supplement companies, food industry

Industry/Entity Type

It Company

Number of Pages Required

4 page

Font styles to use
Sans Serif

Requirements
Must have
• hyperlink to Contact Us page
Nice to have
• pictures

```html
<!DOCTYPE html>
<html lang="en">
<head>
<meta charset="utf-8">
<title>Kestrel Consulting, Inc.</title>
<link href="https://fonts.googleapis.com/css2?family=Open+Sans:ital,wght@0,400;0,600;0,700;1,600&display=swap" rel="stylesheet">
<style>
:root{
  --blue:#0a7cc2;
  --blue-dark:#0868a6;
  --green:#6aa23c;
  --text:#444;
  --muted:#777;
  --page-bg:#eeeeee;
  --panel-bg:#f7f7f7;
  --footer:#333333;
  --footer-bottom:#2a2a2a;
  --yellow:#f3d54a;
}
*{box-sizing:border-box;margin:0;padding:0}
html,body{width:883px;height:1200px;overflow:hidden}
body{font-family:"Open Sans",Arial,sans-serif;background:var(--page-bg);color:var(--text);position:relative}
a{text-decoration:none;color:inherit}
.page{position:absolute;left:110px;top:0;width:662px;height:1000px;background:#fff;box-shadow:0 0 6px rgba(0,0,0,.12)}

/* header */
.brand{position:absolute;left:14px;top:18px;display:flex;align-items:center;gap:8px;font-size:17px;font-weight:700;color:var(--blue)}
.brand-dot{width:30px;height:30px;border-radius:50%;background:var(--green)}
.top-contact{position:absolute;right:16px;top:14px;font-size:8.5px;color:#999}
.top-contact b{font-weight:400;color:#333}
.top-contact span+span{margin-left:12px}
.nav{position:absolute;right:16px;top:41px;display:flex;gap:4px;font-size:8.5px;color:#333}
.nav a{padding:6px 10px;height:21px}
.nav .active{background:#ececec}
.nav .cta{background:var(--blue);color:#fff;display:flex;align-items:center;gap:10px;padding:6px 8px}

/* hero */
.hero{position:absolute;left:0;top:75px;width:662px;height:237px;background:linear-gradient(100deg,#dfe3e8 0%,#f4f5f7 45%,#e9e3dc 70%,#f6f6f6 100%)}
.hero-box{position:absolute;left:147px;top:74px;width:370px;height:116px;background:rgba(255,255,255,.85);text-align:center;padding-top:10px}
.hero-box h1{font-size:16.5px;color:var(--blue);font-weight:700}
.hero-box p{font-size:8.6px;color:#777;line-height:12.5px;margin:2px 14px 0}
.btn{display:inline-block;background:var(--blue);color:#fff;font-size:7.5px;padding:5px 8px;margin-top:6px}

.arrow{position:absolute;width:29px;height:34px}

/* services */
.services-title{position:absolute;left:0;top:338px;width:662px;text-align:center;font-size:18px;font-weight:700;color:var(--blue)}
.services-intro{position:absolute;left:90px;top:364px;width:482px;text-align:center;font-size:7.6px;color:#888;line-height:14px}
.service{position:absolute;top:426px;width:190px;text-align:center}
.service .ring{width:132px;height:132px;border-radius:50%;border:1px solid #e2e2e2;margin:0 auto;padding:6px}
.service .photo{width:118px;height:118px;border-radius:50%}
.service h3{font-size:14px;font-weight:400;color:#333;margin-top:7px}
.service p{font-size:9.4px;line-height:13.5px;color:#666;margin-top:5px}
.service .more{display:inline-flex;align-items:center;gap:4px;font-size:8.8px;color:var(--blue);font-weight:600;margin-top:9px}

/* testimonial */
.testimonial{position:absolute;left:0;top:693px;width:662px;height:159px;background:var(--blue)}
.testimonial-photo{position:absolute;left:0;top:0;width:345px;height:159px;background:linear-gradient(120deg,#d9c2a8,#7fb5d6 50%,#c54a4a 75%,#89b9d9);clip-path:polygon(0 0,280px 0,345px 159px,0 159px)}
.testimonial h2{position:absolute;left:345px;width:258px;top:15px;text-align:center;color:#fff;font-size:15px;font-weight:700}
.testimonial .quote-mark{position:absolute;left:355px;top:53px;color:var(--yellow);font-size:30px;font-weight:700;line-height:30px}
.testimonial blockquote{position:absolute;left:383px;top:66px;width:200px;text-align:center;color:#fff;font-size:9.2px;line-height:15.5px}
.testimonial cite{position:absolute;left:345px;width:258px;top:131px;text-align:center;color:var(--yellow);font-size:8px;font-weight:600}

/* contact strip */
.contact-panel{position:absolute;left:18px;top:876px;width:626px;height:106px;background:var(--panel-bg);border:1px solid #e3e3e3}
.contact-item{position:absolute;top:20px;font-size:7.6px;color:#555;line-height:13.5px}
.contact-item .head{display:flex;align-items:center;gap:8px;color:var(--green);font-size:12.5px;margin-bottom:6px}
.contact-item .head svg{flex:none}
.contact-item a{color:var(--green)}
.subscribe{display:flex;gap:4px;margin-top:3px}
.subscribe .field{width:140px;height:17px;border:1px solid #ddd;background:#fff;font-size:7px;color:#aaa;padding:3px 5px}
.subscribe .go{width:17px;height:17px;background:var(--green)}

/* footer */
.footer{position:absolute;left:0;top:1000px;width:883px;height:163px;background:var(--footer);color:#ccc;font-size:8.3px}
.col{position:absolute;top:34px}
.col h4{color:#fff;font-size:9px;font-weight:600;margin-bottom:10px}
.col li{list-style:none;margin-bottom:5.4px}
.addr{display:flex;gap:7px;margin-bottom:8px;line-height:12.5px}
.follow-note{border-left:1px solid var(--blue);border-right:1px solid var(--blue);padding:4px 8px;line-height:11px;width:140px;margin-left:-1px}
.social{display:block;width:96px;height:13px;margin:3px 0 0 8px;color:#fff;font-size:6px;line-height:13px;padding-left:5px}
.bottom-bar{position:absolute;left:0;top:1163px;width:883px;height:37px;background:var(--footer-bottom);color:#999;font-size:7.5px;text-align:center;line-height:37px}

/* side tabs */
.side-tab{position:absolute;left:773px;width:26px;color:#fff;font-size:8.5px;font-weight:700;writing-mode:vertical-rl;display:flex;align-items:center;justify-content:center;letter-spacing:.5px}
</style>
</head>
<body>
<div class="page">
  <header>
    <a class="brand" href="#"><span class="brand-dot"></span>Kestrel Consulting, Inc.</a>
    <div class="top-contact"><span>Email Us : <b>info@kestrelconsulting.com</b></span><span>Call Us : <b>1800 555 0142</b></span></div>
    <nav class="nav">
      <a class="active" href="#">HOME</a>
      <a href="#">ABOUT US</a>
      <a href="#">OUR SERVICES</a>
      <a class="cta" href="#"><svg width="8" height="8" viewBox="0 0 24 24"><path fill="#fff" d="M6.6 10.8a15 15 0 0 0 6.6 6.6l2.2-2.2c.3-.3.7-.4 1-.2 1.1.4 2.3.6 3.6.6.6 0 1 .4 1 1V20c0 .6-.4 1-1 1A17 17 0 0 1 3 4c0-.6.4-1 1-1h3.5c.6 0 1 .4 1 1 0 1.3.2 2.5.6 3.6.1.3 0 .7-.2 1z"/></svg>CONTACT US</a>
    </nav>
  </header>

  <section class="hero" role="img" aria-label="Doctor with stethoscope reviewing a tablet">
    <div class="hero-box">
      <h1>WELCOME TO KESTREL CONSULTING INC.</h1>
      <p>Lorem ipsum dolor sit amet, consectetur adipiscing elit. Cras tempor sagittis ipsum, in luctus nunc cursus at. Aenean at tortor augue. Duis at sagittis ligula. Pellentesque varius consectetur accumsan. Aenean aliquet tincidunt libero, facilisis tincidunt neque ornare eget.</p>
      <a class="btn" href="#">READ MORE</a>
    </div>
  </section>

  <h2 class="services-title">OUR SERVICES</h2>
  <p class="services-intro">Lorem ipsum dolor sit amet, consectetur adipiscing elit. Nullam egestas fermentum fermentum. Pellentesque vehicula hendrerit elit sed vulputate. Aliquam sed libero dui. Phasellus elementum turpis justo, ut lobortis justo varius at. Quisque eget sagittis turpis.</p>

  <article class="service" style="left:39px">
    <div class="ring"><div class="photo" role="img" aria-label="Abstract molecules in warm tones" style="background:radial-gradient(circle,#e9c98e,#a88a68 60%,#d8b070)"></div></div>
    <h3>Clinical Trial Design</h3>
    <p>Lorem ipsum dolor sit amet, consectetur adipiscing elit. Nullam egestas fermentum fermentum. Pellentesque vehicula hendre-rit elit sed.</p>
    <a class="more" href="#"><svg width="9" height="9" viewBox="0 0 10 10"><circle cx="5" cy="5" r="4.3" fill="none" stroke="#0a7cc2"/><path d="M4 3l2 2-2 2" fill="none" stroke="#0a7cc2" stroke-width="1.2"/></svg>Read More</a>
  </article>
  <article class="service" style="left:236px">
    <div class="ring"><div class="photo" role="img" aria-label="Abstract green data squares" style="background:radial-gradient(circle,#8fc060,#3d7a22 60%,#1f4d12)"></div></div>
    <h3>Clincal Research</h3>
    <p>Lorem ipsum dolor sit amet, consectetur adipiscing elit. Nullam egestas fermentum fermentum. Pellentesque vehicula hendre-rit elit sed.</p>
    <a class="more" href="#"><svg width="9" height="9" viewBox="0 0 10 10"><circle cx="5" cy="5" r="4.3" fill="none" stroke="#0a7cc2"/><path d="M4 3l2 2-2 2" fill="none" stroke="#0a7cc2" stroke-width="1.2"/></svg>Read More</a>
  </article>
  <article class="service" style="left:438px">
    <div class="ring"><div class="photo" role="img" aria-label="Medical professionals attending a lecture" style="background:linear-gradient(160deg,#dfe8f0,#f4f4f4 50%,#c9d6e2)"></div></div>
    <h3>Lcture Service</h3>
    <p>Lorem ipsum dolor sit amet, consectetur adipiscing elit. Nullam egestas fermentum fermentum. Pellentesque vehicula hendre-rit elit sed.</p>
    <a class="more" href="#"><svg width="9" height="9" viewBox="0 0 10 10"><circle cx="5" cy="5" r="4.3" fill="none" stroke="#0a7cc2"/><path d="M4 3l2 2-2 2" fill="none" stroke="#0a7cc2" stroke-width="1.2"/></svg>Read More</a>
  </article>

  <section class="testimonial">
    <div class="testimonial-photo" role="img" aria-label="Hand holding a stethoscope to a red heart on a tablet"></div>
    <h2>WHO LOVES OUR SERVICES</h2>
    <svg style="position:absolute;left:462px;top:42px" width="24" height="20" viewBox="0 0 24 20"><path fill="#fff" d="M12 20L2 10A6 6 0 0 1 12 3a6 6 0 0 1 10 7z"/></svg>
    <div class="quote-mark">&ldquo;</div>
    <blockquote>Nunc eleifend, magna et efficitur efficitur, ipsum nisl facilisis lorem, ac iaculis metus tellus quis nibh. Aenean malesuada tortor elit, quis com-modo dui euismod vel.</blockquote>
    <cite>[ Mark Ellis, A Lorem Ipsum Co. ]</cite>
  </section>

  <section class="contact-panel">
    <div class="contact-item" style="left:21px">
      <div class="head"><svg width="22" height="22" viewBox="0 0 22 22"><circle cx="11" cy="11" r="10" fill="none" stroke="#6aa23c" stroke-width="1.5"/><path fill="#6aa23c" d="M8 6.5l1.6 2.2-1 1.1a6 6 0 0 0 3.6 3.6l1.1-1 2.2 1.6-.9 1.5C10.5 15.6 6.4 11.5 6.5 7.4z"/></svg>(888) 555-0193</div>
      We're here to answer any questions you have.<br>Friendly staff are standing by. <a href="#">Contact us</a> today.
    </div>
    <div class="contact-item" style="left:226px">
      <div class="head"><svg width="22" height="22" viewBox="0 0 22 22"><circle cx="11" cy="11" r="10" fill="none" stroke="#6aa23c" stroke-width="1.5"/><rect x="6" y="7.5" width="10" height="7" fill="#6aa23c"/><path d="M6 7.5l5 4 5-4" fill="none" stroke="#fff"/></svg>Stay Connected</div>
      Subscribe to our newsletter to keep you update
      <div class="subscribe"><div class="field">Your Email</div><div class="go"><svg width="17" height="17" viewBox="0 0 17 17"><path d="M7 5l3.5 3.5L7 12" fill="none" stroke="#fff" stroke-width="1.6"/></svg></div></div>
    </div>
    <div class="contact-item" style="left:421px">
      <div class="head"><svg width="22" height="22" viewBox="0 0 22 22"><circle cx="11" cy="11" r="10" fill="none" stroke="#6aa23c" stroke-width="1.5"/><path d="M7 15l5-5M12 10a2.5 2.5 0 1 0 2.5-3" fill="none" stroke="#6aa23c" stroke-width="1.8"/></svg>info@kestrelconsulting.com</div>
      Need assistance with Tech Support? Give us a<br>call.
    </div>
  </section>
</div>

<svg class="arrow" style="left:104px;top:174px" viewBox="0 0 29 34"><path d="M0 0h29v34H0z" fill="#6aa23c"/><path d="M0 0l5 4v26l-5 4z" fill="#4f8128"/><path d="M18 10l-7 7 7 7" fill="none" stroke="#fff" stroke-width="3.5"/></svg>
<svg class="arrow" style="left:750px;top:174px" viewBox="0 0 29 34"><path d="M0 0h29v34H0z" fill="#6aa23c"/><path d="M29 0l-5 4v26l5 4z" fill="#4f8128"/><path d="M11 10l7 7-7 7" fill="none" stroke="#fff" stroke-width="3.5"/></svg>
<svg class="arrow" style="left:104px;top:541px" viewBox="0 0 29 34"><path d="M0 0h29v34H0z" fill="#6aa23c"/><path d="M0 0l5 4v26l-5 4z" fill="#4f8128"/><path d="M18 10l-7 7 7 7" fill="none" stroke="#fff" stroke-width="3.5"/></svg>
<svg class="arrow" style="left:750px;top:541px" viewBox="0 0 29 34"><path d="M0 0h29v34H0z" fill="#6aa23c"/><path d="M29 0l-5 4v26l5 4z" fill="#4f8128"/><path d="M11 10l7 7-7 7" fill="none" stroke="#fff" stroke-width="3.5"/></svg>

<a class="side-tab" href="#" style="top:241px;height:80px;background:var(--blue)">CONTACT US</a>
<a class="side-tab" href="#" style="top:327px;height:98px;background:var(--green)">ENQUIRY NOW</a>

<footer class="footer">
  <div class="col" style="left:128px"><h4>Useful Links</h4><ul><li>Home</li><li>About Us</li><li>Services</li><li>Contact Us</li><li>Privacy Policy</li></ul></div>
  <div class="col" style="left:271px"><h4>Our Services</h4><ul><li>Clinical Trial Design</li><li>Clincal Research</li><li>Product Safety</li><li>Claim Development Strategy</li><li>Lecture Service</li></ul></div>
  <div class="col" style="left:455px"><h4>Contact Us</h4>
    <div class="addr"><svg width="7" height="9" viewBox="0 0 7 9"><path d="M3.5 0A3.5 3.5 0 0 0 0 3.5C0 6 3.5 9 3.5 9S7 6 7 3.5A3.5 3.5 0 0 0 3.5 0z" fill="#ccc"/></svg><span>Kestrel Consulting<br>123, A Lorem Ipsum<br>Dolor Sit, USA</span></div>
    <div class="addr"><svg width="9" height="9" viewBox="0 0 24 24"><path fill="#ccc" d="M6.6 10.8a15 15 0 0 0 6.6 6.6l2.2-2.2c.3-.3.7-.4 1-.2 1.1.4 2.3.6 3.6.6.6 0 1 .4 1 1V20c0 .6-.4 1-1 1A17 17 0 0 1 3 4c0-.6.4-1 1-1h3.5c.6 0 1 .4 1 1 0 1.3.2 2.5.6 3.6.1.3 0 .7-.2 1z"/></svg>1800 555 0142</div>
    <div class="addr"><svg width="9" height="7" viewBox="0 0 9 7"><rect width="9" height="7" fill="#ccc"/><path d="M0 0l4.5 4L9 0" fill="none" stroke="#333"/></svg>support@kestrelconsulting.com</div>
  </div>
  <div class="col" style="left:615px"><h4>Follow Us</h4>
    <div class="follow-note">We are social at the below social media website. Please follow.</div>
    <a class="social" href="#" style="background:#4aa8e0">FOLLOW US ON CHIRPLINE</a>
    <a class="social" href="#" style="background:#1b7fb5">FOLLOW US ON PROLINK</a>
    <a class="social" href="#" style="background:#4a66a8">LIKE US ON FRIENDBOOK</a>
  </div>
</footer>
<div class="bottom-bar">&copy; 2006-2014 Kestrel Consulting, Inc. All rights reserved.</div>
</body>
</html>
```